Design a Mobile First Website for a Salad Resturant

** WEBSITE LIKE AN APP, NOT LANDING PAGE **

1. Homepage
Objective: Introduce the brand and direct visitors to either start creating their custom salad or explore the menu of pre-designed salads.
Design Elements:
Clean and minimalistic layout with high-quality images of fresh salads.
Two prominent buttons: "Create Your Salad" and "Our Salads".
Brief welcome message that highlights the freshness and quality of ingredients.

2. Create Your Salad Page
Objective: Allow customers to design their salad from a list of ingredients.
Design Elements:
Interactive, step-by-step builder interface where customers can select ingredients. Each ingredient category (like greens, proteins, toppings, dressings) should be a separate step in the process.
Visual representation of their salad being built as they select ingredients.
Information icons next to each ingredient for dietary information (e.g., vegan, gluten-free, calories).
Option to save favorite combinations or reorder past salads.
Clear price updates as they add or remove ingredients.

3. Our Salads Page
Objective: Showcase a list of pre-designed salad options that customers can quickly choose from.
Design Elements:
Grid layout with images and brief descriptions of each pre-designed salad.
Include customer reviews and ratings for each salad.
Easy "Add to Cart" option from this page.

4. Cart and Checkout Page
Objective: Streamline the checkout process with minimal steps.
Design Elements:
Summary of order with options to modify quantities or remove items.
Simple form for entering delivery details, with the ability to remember details for returning customers.
Secure payment gateway integration.
A confirmation screen with estimated delivery time and order tracking capabilities.

5. Mobile Optimization
Approach: Since this is a "Mobile First Design", ensure that:
The website is responsive and elements like buttons, text, and images scale properly across different devices.
Touch-friendly interfaces with large tap targets for ease of use on mobile devices.
Fast loading times by optimizing images and using mobile-first coding practices.

Target Market(s)

Food

Industry/Entity Type

Food

Number of Pages Required

4 page

Requirements
Must have
• Modren Design, Mobile First

```html
<!DOCTYPE html>
<html lang="en">
<head>
<meta charset="utf-8">
<title>Greenbowl – Salad App Screens</title>
<link href="https://fonts.googleapis.com/css2?family=Lexend:wght@300;400;500;600;700&display=swap" rel="stylesheet">
<style>
:root{
  --slate:#4a5f78;
  --ink:#3e4b5e;
  --ink-soft:#6b7482;
  --sage:#a9b67a;
  --muted:#a3a9b1;
  --line:#e3e5e8;
  --paper:#ffffff;
  --panel:#ecedee;
  --logo-ghost:#8e99a4;
  --star:#f1b23c;
  --bookmark:#f6c15a;
}
*{margin:0;padding:0;box-sizing:border-box}
html,body{width:813px;height:1200px;overflow:hidden;background:var(--slate)}
body{font-family:'Lexend',sans-serif;color:var(--ink)}
.board{position:relative;width:813px;height:1200px;background:var(--slate);overflow:hidden}
.screen{position:absolute;top:115px;width:122px;background:var(--paper);border-radius:13px;overflow:hidden}
.a{position:absolute}
.time{left:13px;top:6px;font-size:5.5px;font-weight:600}
.island{left:42px;top:3px;width:39px;height:11px;border-radius:6px;background:#111}
.sys{right:11px;top:6px;width:20px;height:5px}
.home-bar{left:37px;bottom:4px;width:48px;height:1.5px;border-radius:1px;background:#222}
.back{left:6px;top:26px;width:9px;height:9px}
.page-title{right:6px;top:26px;font-size:7.5px;font-weight:600;color:var(--ink)}
.tiny{font-size:2.4px;line-height:3.2px;color:var(--muted)}
.btn{background:var(--sage);color:#fff;border-radius:2px;font-size:3px;display:flex;align-items:center;justify-content:center}
.splash-bg{inset:0;background:linear-gradient(180deg,#f3f2ee 0%,#ecebe6 45%,#d9d6cc 100%)}
.splash-bowl{left:0;top:122px;width:122px;height:143px;background:radial-gradient(ellipse at 55% 55%,#9aa55a 0%,#6f7f3c 38%,#5b4c3a 62%,#d9c4b2 80%,#e6e3dd 100%)}
.brand{width:122px;text-align:center;font-weight:600;color:var(--ink)}
.chip{top:77px;height:7px;border:.5px solid var(--ink);border-radius:4px;font-size:2.8px;display:flex;align-items:center;justify-content:center}
.chip.on{background:var(--sage);border-color:var(--sage);color:#fff}
.feature{left:6px;width:110px;border-radius:4px;background:#fff;box-shadow:0 1px 3px rgba(0,0,0,.12);overflow:hidden}
.feature h3{position:absolute;left:4px;font-size:5.5px;font-weight:500}
.rec{left:6px;width:110px;height:31px;border-radius:3px;background:linear-gradient(90deg,#f3f3f5,#fafafa);box-shadow:0 1px 2px rgba(0,0,0,.08)}
.rec-meta{left:6px;width:110px;font-size:3px;display:flex;justify-content:space-between}
.rec-meta .rate{color:var(--star)}
.bowl{border-radius:50%;background:radial-gradient(circle at 45% 40%,#b7c56a 0%,#d07a3c 35%,#8a9f4a 55%,#c9b59a 75%,#b8a48a 100%)}
.kcal{font-size:2.8px;color:var(--ink-soft)}
.dish{font-size:5px;font-weight:600;white-space:nowrap}
.stat{font-size:2.8px;color:var(--muted)}
.sec{left:6px;font-size:4.8px;display:flex;align-items:center;gap:2px}
.sec i{display:inline-block;width:4px;height:4px;border:.4px solid var(--ink);border-radius:50%;font-style:normal;font-size:2.4px;text-align:center;line-height:3.4px}
.ing{width:27px;height:36px;border-radius:2px;background:#fff;box-shadow:0 .5px 2px rgba(0,0,0,.15)}
.ing.on{background:var(--sage)}
.ing .pic{position:absolute;left:6px;top:-6px;width:15px;height:14px;border-radius:50%}
.ing .nm{position:absolute;left:0;right:0;top:12px;text-align:center;font-size:2.2px;white-space:nowrap;overflow:hidden}
.ing .tg{position:absolute;left:3px;top:17px;font-size:2px;line-height:3px;color:var(--muted)}
.ing.on .nm,.ing.on .tg{color:#fff}
.dot{width:5px;height:5px;border-radius:50%;border:.5px solid var(--sage);font-size:1.8px;color:var(--sage);display:flex;align-items:center;justify-content:center}
.dot.on{background:var(--sage);color:#fff}
.menu-card{left:6px;width:111px;height:75px;border-radius:3px;box-shadow:0 1px 3px rgba(0,0,0,.12);overflow:hidden}
.avatar{width:11px;height:11px;border-radius:50%;background:#b8a594}
.order-name{left:50px;font-size:5px;font-weight:500;white-space:nowrap}
.order-price{left:50px;font-size:5px;font-weight:500}
.order-price span{font-size:3px;color:var(--muted);font-weight:300}
.qty{display:flex;align-items:center;gap:2px}
.qty b{width:6px;height:6px;border-radius:50%;background:var(--ink);color:#fff;font-size:5px;line-height:5.5px;text-align:center;font-weight:400}
.qty span{width:10px;height:6px;border:.5px solid var(--ink);border-radius:1.5px;font-size:3.6px;text-align:center;line-height:5px}
.field{height:12px;border:.5px solid #d8dadd;border-radius:2px;background:#fff;font-size:3px;color:var(--muted);padding:4px 3px}
.sum{left:6px;right:6px;display:flex;justify-content:space-between;font-size:5px;color:var(--ink-soft);font-weight:300}
.card-holder{left:8px;top:60px;font-size:3.4px;font-weight:500;letter-spacing:.2px;white-space:nowrap}
.ghost-mark{left:0;width:813px;text-align:center;font-weight:600;color:var(--logo-ghost)}
</style>
</head>
<body>
<main class="board">

  <section class="screen" style="left:15px;height:265px">
    <div class="a splash-bg" role="img" aria-label="Photo of fresh salad on a light marble table with lemon wedges"></div>
    <div class="a splash-bowl" role="img" aria-label="Hands holding a bowl of chickpeas, avocado, corn, greens and grains"></div>
    <div class="a time">9:41</div><div class="a island"></div>
    <svg class="a sys" viewBox="0 0 20 5"><rect x="0" y="3" width="1" height="2" fill="#222"/><rect x="1.6" y="2" width="1" height="3" fill="#222"/><rect x="3.2" y="1" width="1" height="4" fill="#222"/><path d="M7 2.2a3 3 0 0 1 4 0l-2 2.3z" fill="#222"/><rect x="13" y="1" width="6" height="3.4" rx=".8" fill="#222"/></svg>
    <div class="a brand" style="top:63px;font-size:17px">Greenbowl</div>
    <div class="a brand" style="top:84px;font-size:4.5px;font-weight:300">Greens Come True!</div>
    <div class="a brand" style="top:102px;font-size:5.6px;font-weight:300;line-height:7px">“Greens produce results.<br>Dreams don’t.”</div>
    <div class="a home-bar"></div>
  </section>

  <section class="screen" style="left:147px;height:596px">
    <div class="a time">9:41</div><div class="a island"></div>
    <svg class="a sys" viewBox="0 0 20 5"><rect x="0" y="3" width="1" height="2" fill="#222"/><rect x="1.6" y="2" width="1" height="3" fill="#222"/><rect x="3.2" y="1" width="1" height="4" fill="#222"/><path d="M7 2.2a3 3 0 0 1 4 0l-2 2.3z" fill="#222"/><rect x="13" y="1" width="6" height="3.4" rx=".8" fill="#222"/></svg>
    <div class="a tiny" style="left:6px;top:27px">Hello</div>
    <div class="a" style="left:6px;top:32px;font-size:3.8px">Mara Quill</div>
    <div class="a avatar" role="img" aria-label="User profile photo" style="left:103px;top:24px;width:12px;height:12px;border:1px solid #ddd"></div>
    <div class="a" style="left:0;top:42px;width:122px;height:.5px;background:var(--line)"></div>
    <div class="a" style="left:6px;width:110px;top:54px;text-align:center;font-size:3.3px;line-height:4.2px;font-weight:600">Welcome to <span style="color:var(--sage)">Greenbowl!</span><br>Discover the delicious difference with our fresh,<br>top-quality ingredients. Start exploring now!”</div>
    <div class="a chip" style="left:6px;width:28px">Favorites</div>
    <div class="a chip on" style="left:39px;width:28px">Vegan</div>
    <div class="a chip" style="left:72px;width:28px">Gluten - Free</div>
    <div class="a chip" style="left:104px;width:28px">Low Cal</div>

    <div class="a feature" style="top:93px;height:96px">
      <div class="a" role="img" aria-label="Photo of hands tossing a green salad in a glass bowl" style="left:0;top:0;width:110px;height:53px;background:linear-gradient(135deg,#d9dad4,#9fb36a 55%,#e6e4dc)"></div>
      <h3 style="top:59px">Create Your Salad</h3>
      <div class="a tiny" style="left:4px;top:68px;width:100px">Make your perfect salad with mixed greens, veggies, protein of choice, your favorite dressing, and a sprinkle of fresh herbs.</div>
      <div class="a btn" style="left:4px;top:81px;width:31px;height:8px">Create Now</div>
      <div class="a tiny" style="right:4px;top:86px">$2 Delivery</div>
    </div>
    <div class="a feature" style="top:199px;height:94px">
      <div class="a" role="img" aria-label="Photo of a colourful salad bar with many chopped vegetables" style="left:0;top:0;width:110px;height:53px;background:linear-gradient(90deg,#c9473a,#6f9a3c 30%,#e89a3a 55%,#8b2f44 75%,#d8d2c4)"></div>
      <h3 style="top:59px">Our Salad</h3>
      <div class="a tiny" style="left:4px;top:68px;width:104px">Crafting our salads involves a medley of vibrant vegetables, a protein source, dressing preference, and a final flourish of fresh herbs.</div>
      <div class="a btn" style="left:4px;top:80px;width:31px;height:8px">Shop Now</div>
      <div class="a tiny" style="right:4px;top:85px">Free Delivery</div>
    </div>

    <div class="a" style="left:6px;top:308px;font-size:3.6px;color:var(--ink-soft)">Recommended for you</div>

    <div class="a rec-meta" style="top:320px"><span class="rate">★ 4.5</span><span>$15</span></div>
    <div class="a rec" style="top:325px"><div class="a bowl" role="img" aria-label="Salad bowl photo" style="left:6px;top:2px;width:29px;height:27px"></div><div class="a kcal" style="left:58px;top:7px">311 KCAL</div><div class="a dish" style="left:58px;top:11px">Dream on Salad</div><div class="a stat" style="left:58px;top:19px">36 SR &nbsp; 27 SR</div></div>

    <div class="a rec-meta" style="top:366px"><span class="rate">★ 4.2</span><span>$12</span></div>
    <div class="a rec" style="top:371px"><div class="a kcal" style="left:8px;top:7px">311 KCAL</div><div class="a dish" style="left:8px;top:11px">Kale Ceasar Salad</div><div class="a stat" style="left:8px;top:19px">35 SR &nbsp; 27 SR</div><div class="a bowl" role="img" aria-label="Salad bowl photo" style="left:76px;top:2px;width:29px;height:27px"></div></div>

    <div class="a rec-meta" style="top:411px"><span class="rate">★ 4.2</span><span>$20</span></div>
    <div class="a rec" style="top:416px"><div class="a bowl" role="img" aria-label="Salad bowl photo" style="left:6px;top:2px;width:29px;height:27px"></div><div class="a kcal" style="left:58px;top:7px">311 KCAL</div><div class="a dish" style="left:58px;top:11px">True Salad</div><div class="a stat" style="left:58px;top:19px">35 SR &nbsp; 27 SR</div></div>

    <div class="a rec-meta" style="top:457px"><span class="rate">★ 4.2</span><span>$15</span></div>
    <div class="a rec" style="top:462px"><div class="a kcal" style="left:8px;top:7px">311 KCAL</div><div class="a dish" style="left:8px;top:11px">Halloumi Salad</div><div class="a stat" style="left:8px;top:19px">36 SR &nbsp; 27 SR</div><div class="a bowl" role="img" aria-label="Salad bowl photo" style="left:76px;top:2px;width:29px;height:27px"></div></div>

    <div class="a rec-meta" style="top:502px"><span class="rate">★ 4.2</span><span>$12</span></div>
    <div class="a rec" style="top:507px;background:linear-gradient(90deg,#fdf1de,#fafafa)"><div class="a bowl" role="img" aria-label="Salad bowl photo" style="left:6px;top:2px;width:29px;height:27px"></div><div class="a kcal" style="left:60px;top:7px">311 KCAL</div><div class="a dish" style="left:60px;top:11px">Korean Salad</div><div class="a stat" style="left:60px;top:19px">35 SR &nbsp; 27 SR</div></div>

    <div class="a rec-meta" style="top:548px"><span class="rate">★ 4.2</span><span>$15</span></div>
    <div class="a rec" style="top:553px;background:linear-gradient(90deg,#fafafa,#fbe3dc)"><div class="a kcal" style="left:8px;top:7px">311 KCAL</div><div class="a dish" style="left:8px;top:11px">Crab Salad</div><div class="a stat" style="left:8px;top:19px">36 SR &nbsp; 27 SR</div><div class="a bowl" role="img" aria-label="Salad bowl photo" style="left:76px;top:2px;width:29px;height:27px"></div></div>
  </section>

  <section class="screen" style="left:279px;height:432px">
    <div class="a time">9:41</div><div class="a island"></div>
    <svg class="a sys" viewBox="0 0 20 5"><rect x="0" y="3" width="1" height="2" fill="#222"/><rect x="1.6" y="2" width="1" height="3" fill="#222"/><rect x="3.2" y="1" width="1" height="4" fill="#222"/><path d="M7 2.2a3 3 0 0 1 4 0l-2 2.3z" fill="#222"/><rect x="13" y="1" width="6" height="3.4" rx=".8" fill="#222"/></svg>
    <svg class="a back" viewBox="0 0 10 10"><circle cx="5" cy="5" r="4.5" fill="none" stroke="#9aa1aa" stroke-width=".5"/><path d="M6.5 5H3.5M5 3.5 3.5 5 5 6.5" fill="none" stroke="#9aa1aa" stroke-width=".5"/></svg>
    <div class="a page-title">Create Your Salad</div>
    <div class="a" role="img" aria-label="Photo of a fresh green salad with tomato on a white plate" style="left:22px;top:41px;width:78px;height:48px;border-radius:50%;background:radial-gradient(ellipse at 50% 40%,#8fcf45 0%,#5ea42f 45%,#d9d9d9 72%,#f1f1f1 100%)"></div>
    <svg class="a" style="left:112px;top:46px;width:5px;height:7px" viewBox="0 0 5 7"><path d="M0 0h5v7L2.5 5 0 7z" fill="var(--bookmark)"/></svg>
    <div class="a qty" style="left:6px;top:92px"><b>+</b><span>2</span><b>–</b></div>
    <div class="a tiny" style="left:16px;top:100px;font-size:1.8px">Quantity</div>
    <div class="a" style="right:6px;top:92px;font-size:5.5px">Total: $8</div>
    <div class="a" style="left:0;top:104px;width:122px;height:5px;background:linear-gradient(#f4f4f4,#fff)"></div>
    <div class="a tiny" style="left:6px;top:111px;font-size:2.2px">Please select your ingredients</div>

    <div class="a sec" style="top:121px"><i>1</i>Select your Greens</div>
    <div class="a ing" style="left:-11px;top:132px"><div class="pic" style="background:#5fa33a"></div><div class="nm">Lettuce</div><div class="tg">Vegan<br>Gluten free<br>20</div></div>
    <div class="a ing on" style="left:15px;top:132px"><div class="pic" style="background:#3f8f2c"></div><div class="nm">Winter Spinach</div><div class="tg">Vegan<br>Gluten free<br>20</div></div>
    <div class="a ing" style="left:46px;top:132px"><div class="pic" style="background:#4e9a34"></div><div class="nm">Butterhead</div><div class="tg">Vegan<br>Gluten free<br>20</div></div>
    <div class="a ing" style="left:77px;top:132px"><div class="pic" style="background:#2f7d3a"></div><div class="nm">Iceberg Lettuce</div><div class="tg">Vegan<br>Gluten free<br>20</div></div>
    <div class="a ing" style="left:108px;top:132px"><div class="pic" style="background:#3a7a2a"></div><div class="nm">Spinach</div><div class="tg">Vegan<br>Gluten free<br>20</div></div>
    <div class="a dot" style="left:-3px;top:170px">$1</div><div class="a dot on" style="left:26px;top:170px">$1</div><div class="a dot" style="left:57px;top:170px">$1</div><div class="a dot" style="left:88px;top:170px">$1</div><div class="a dot" style="left:119px;top:170px">$1</div>

    <div class="a sec" style="top:194px"><i>2</i>Select your Proteins</div>
    <div class="a ing on" style="left:6px;top:210px;height:34px"><div class="pic" style="background:#e9a58f"></div><div class="nm">Chicken Breast</div><div class="tg">Vegan<br>Gluten free<br>20</div></div>
    <div class="a ing" style="left:37px;top:210px;height:34px"><div class="pic" style="background:#86b34a"></div><div class="nm">Lentils</div><div class="tg">Vegan<br>Gluten free<br>20</div></div>
    <div class="a ing" style="left:68px;top:210px;height:34px"><div class="pic" style="background:#ede6cf"></div><div class="nm">Tofu</div><div class="tg">Vegan<br>Gluten free<br>20</div></div>
    <div class="a ing" style="left:99px;top:210px;height:34px"><div class="pic" style="background:#e7ddcc"></div><div class="nm">Mushroom</div><div class="tg">Vegan<br>Gluten free<br>20</div></div>
    <div class="a dot" style="left:17px;top:247px">$1</div><div class="a dot" style="left:48px;top:247px">$1</div><div class="a dot" style="left:79px;top:247px">$1</div><div class="a dot" style="left:110px;top:247px">$1</div>

    <div class="a sec" style="top:262px"><i>3</i>Select your Toppings</div>
    <div class="a ing" style="left:-1px;top:278px"><div class="pic" style="background:#b0702f"></div><div class="nm">Mixed Nuts</div><div class="tg">Vegan<br>Gluten free<br>20</div></div>
    <div class="a ing" style="left:30px;top:278px"><div class="pic" style="background:#8a2a3a"></div><div class="nm">Dried Fruits</div><div class="tg">Vegan<br>Gluten free<br>20</div></div>
    <div class="a ing" style="left:61px;top:278px"><div class="pic" style="background:#d8c08a"></div><div class="nm">Whole Grains</div><div class="tg">Vegan<br>Gluten free<br>20</div></div>
    <div class="a ing on" style="left:92px;top:278px"><div class="pic" style="background:#d94f3a"></div><div class="nm">Fresh Fruits</div><div class="tg">Vegan<br>Gluten free<br>20</div></div>
    <div class="a dot" style="left:10px;top:316px">$1</div><div class="a dot" style="left:41px;top:316px">$1</div><div class="a dot" style="left:72px;top:316px">$1</div><div class="a dot on" style="left:103px;top:316px">$1</div>

    <div class="a sec" style="top:331px"><i>4</i>Select your Dressings</div>
    <div class="a ing" style="left:-1px;top:347px"><div class="pic" style="background:#b89a1c"></div><div class="nm">Honey Mustard</div><div class="tg">Vegan<br>Gluten free<br>20</div></div>
    <div class="a ing on" style="left:30px;top:347px"><div class="pic" style="background:#a88d18"></div><div class="nm">Balsamic</div><div class="tg">Vegan<br>Gluten free<br>20</div></div>
    <div class="a ing" style="left:61px;top:347px"><div class="pic" style="background:#b8961e"></div><div class="nm">Ranch</div><div class="tg">Vegan<br>Gluten free<br>20</div></div>
    <div class="a ing" style="left:92px;top:347px"><div class="pic" style="background:#a8901a"></div><div class="nm">Walnut</div><div class="tg">Vegan<br>Gluten free<br>20</div></div>
    <div class="a dot" style="left:10px;top:385px">$1</div><div class="a dot on" style="left:41px;top:385px">$1</div><div class="a dot" style="left:72px;top:385px">$1</div><div class="a dot" style="left:103px;top:385px">$1</div>

    <div class="a btn" style="left:6px;top:407px;width:110px;height:13px;font-size:5px;font-weight:500">Proceed to Checkout</div>
  </section>

  <section class="screen" style="left:412px;height:537px">
    <div class="a time">9:41</div><div class="a island"></div>
    <svg class="a sys" viewBox="0 0 20 5"><rect x="0" y="3" width="1" height="2" fill="#222"/><rect x="1.6" y="2" width="1" height="3" fill="#222"/><rect x="3.2" y="1" width="1" height="4" fill="#222"/><path d="M7 2.2a3 3 0 0 1 4 0l-2 2.3z" fill="#222"/><rect x="13" y="1" width="6" height="3.4" rx=".8" fill="#222"/></svg>
    <svg class="a back" viewBox="0 0 10 10"><circle cx="5" cy="5" r="4.5" fill="none" stroke="#9aa1aa" stroke-width=".5"/><path d="M6.5 5H3.5M5 3.5 3.5 5 5 6.5" fill="none" stroke="#9aa1aa" stroke-width=".5"/></svg>
    <div class="a page-title">Our Salad</div>

    <article class="a menu-card" style="top:41px;background:linear-gradient(90deg,#f1f1f3,#fafafa)">
      <div class="a bowl" role="img" aria-label="Dream on Salad bowl photo" style="left:5px;top:4px;width:34px;height:28px"></div>
      <div class="a kcal" style="left:49px;top:7px">311 KCAL</div><div class="a kcal" style="right:5px;top:7px">$15</div>
      <div class="a dish" style="left:49px;top:12px">Dream on Salad</div><div class="a stat" style="left:49px;top:20px">36 SR &nbsp; 27 SR</div>
      <div class="a tiny" style="left:6px;top:35px;width:100px">The Dream On Salad features a refreshing mix of mixed greens, ripe strawberries, creamy goat cheese crumbles, crunchy candied pecans and tangy balsamic vinaigrette creating a delightful harmony of sweet, savory and nutty flavors.</div>
      <div class="a avatar" role="img" aria-label="Reviewer photo" style="left:6px;top:55px"></div>
      <div class="a tiny" style="left:22px;top:54px">“Taste very delicious I love it”</div>
      <div class="a" style="left:22px;top:63px;font-size:2.6px;color:var(--star)">★ 4.5</div><div class="a" style="left:52px;top:63px;font-size:2.4px">Wren</div>
      <div class="a btn" style="left:81px;top:58px;width:25px;height:8px;font-size:2.4px">Add to Cart</div>
    </article>

    <article class="a menu-card" style="top:122px;background:linear-gradient(90deg,#f4f5ee,#fafafa)">
      <div class="a bowl" role="img" aria-label="Kale Ceasar Salad bowl photo" style="left:5px;top:4px;width:34px;height:28px"></div>
      <div class="a kcal" style="left:49px;top:7px">311 KCAL</div><div class="a kcal" style="right:5px;top:7px">$12</div>
      <div class="a dish" style="left:49px;top:12px">Kale Ceasar Salad</div><div class="a stat" style="left:49px;top:20px">36 SR &nbsp; 27 SR</div>
      <div class="a tiny" style="left:6px;top:35px;width:100px">The Kale Caesar Salad boasts a robust combination of nutrient-rich kale coated in creamy Caesar dressing, generous shavings of parmesan cheese, and a hint of freshly ground black pepper.</div>
      <div class="a avatar" role="img" aria-label="Reviewer photo" style="left:6px;top:55px"></div>
      <div class="a tiny" style="left:22px;top:54px">“The vegetables are all fresh.”</div>
      <div class="a" style="left:22px;top:63px;font-size:2.6px;color:var(--star)">★ 4.2</div><div class="a" style="left:52px;top:63px;font-size:2.4px">Ines</div>
      <div class="a btn" style="left:81px;top:58px;width:25px;height:8px;font-size:2.4px">Add to Cart</div>
    </article>

    <article class="a menu-card" style="top:204px;background:linear-gradient(90deg,#e9ebef,#fafafa)">
      <div class="a bowl" role="img" aria-label="True Salad bowl photo" style="left:5px;top:4px;width:34px;height:28px"></div>
      <div class="a kcal" style="left:49px;top:7px">311 KCAL</div><div class="a kcal" style="right:5px;top:7px">$20</div>
      <div class="a dish" style="left:49px;top:12px">True Salad</div><div class="a stat" style="left:49px;top:20px">36 SR &nbsp; 27 SR</div>
      <div class="a tiny" style="left:6px;top:35px;width:100px">The True Salad offers a vibrant medley of mixed greens, juicy cherry tomatoes, crisp cucumber slices, shredded carrots and tangy red onion, tied together with a zesty lemon vinaigrette.</div>
      <div class="a avatar" role="img" aria-label="Reviewer photo" style="left:6px;top:55px"></div>
      <div class="a tiny" style="left:22px;top:54px">“A refreshing and satisfying<br>choice on hot days.”</div>
      <div class="a" style="left:22px;top:63px;font-size:2.6px;color:var(--star)">★ 4.2</div><div class="a" style="left:52px;top:63px;font-size:2.4px">Oli</div>
      <div class="a btn" style="left:81px;top:58px;width:25px;height:8px;font-size:2.4px">Add to Cart</div>
    </article>

    <article class="a menu-card" style="top:285px;background:linear-gradient(90deg,#f3f3f5,#fafafa)">
      <div class="a bowl" role="img" aria-label="Halloumi Salad bowl photo" style="left:5px;top:4px;width:34px;height:28px"></div>
      <div class="a kcal" style="left:49px;top:7px">311 KCAL</div><div class="a kcal" style="right:5px;top:7px">$15</div>
      <div class="a dish" style="left:49px;top:12px">Halloumi Salad</div><div class="a stat" style="left:49px;top:20px">36 SR &nbsp; 27 SR</div>
      <div class="a tiny" style="left:6px;top:35px;width:100px">The Halloumi Salad presents a tantalizing fusion of grilled halloumi cheese atop a bed of mixed greens, juicy cherry tomatoes, creamy avocado and crunchy cucumber with a tangy dressing.</div>
      <div class="a avatar" role="img" aria-label="Reviewer photo" style="left:6px;top:55px"></div>
      <div class="a tiny" style="left:22px;top:54px">“The halloumi grilled well,<br>flavour packed delight.”</div>
      <div class="a" style="left:22px;top:63px;font-size:2.6px;color:var(--star)">★ 4.2</div><div class="a" style="left:52px;top:63px;font-size:2.4px">Bram</div>
      <div class="a btn" style="left:81px;top:58px;width:25px;height:8px;font-size:2.4px">Add to Cart</div>
    </article>

    <article class="a menu-card" style="top:367px;background:linear-gradient(90deg,#fdf1de,#fafafa)">
      <div class="a bowl" role="img" aria-label="Korean Salad bowl photo" style="left:5px;top:4px;width:34px;height:28px"></div>
      <div class="a kcal" style="left:49px;top:7px">311 KCAL</div><div class="a kcal" style="right:5px;top:7px">$12</div>
      <div class="a dish" style="left:49px;top:12px">Korean Salad</div><div class="a stat" style="left:49px;top:20px">36 SR &nbsp; 27 SR</div>
      <div class="a tiny" style="left:6px;top:35px;width:100px">The Korean Salad offers a unique blend of fresh vegetables such as crunchy lettuce, shredded carrots and crisp cucumber, topped with marinated bulgogi beef or tofu and toasted sesame seeds.</div>
      <div class="a avatar" role="img" aria-label="Reviewer photo" style="left:6px;top:55px"></div>
      <div class="a tiny" style="left:22px;top:54px">“A delightful explosion of flavors, with<br>the perfect balance of freshness.”</div>
      <div class="a" style="left:22px;top:63px;font-size:2.6px;color:var(--star)">★ 4.2</div><div class="a" style="left:52px;top:63px;font-size:2.4px">Teo</div>
      <div class="a btn" style="left:81px;top:58px;width:25px;height:8px;font-size:2.4px">Add to Cart</div>
    </article>

    <article class="a menu-card" style="top:448px;background:linear-gradient(90deg,#fbe3dc,#fafafa)">
      <div class="a bowl" role="img" aria-label="Crab Salad bowl photo" style="left:5px;top:4px;width:34px;height:28px"></div>
      <div class="a kcal" style="left:49px;top:7px">311 KCAL</div><div class="a kcal" style="right:5px;top:7px">$15</div>
      <div class="a dish" style="left:49px;top:12px">Crab Salad</div><div class="a stat" style="left:49px;top:20px">36 SR &nbsp; 27 SR</div>
      <div class="a tiny" style="left:6px;top:35px;width:100px">The Crab Salad offers a delectable combination of succulent crab meat tossed with crisp lettuce, diced cucumber, creamy avocado and zesty lemon dressing for an indulgent seafood experience.</div>
      <div class="a avatar" role="img" aria-label="Reviewer photo" style="left:6px;top:55px"></div>
      <div class="a tiny" style="left:22px;top:54px">“The Crab Salad was a culinary<br>masterpiece.”</div>
      <div class="a" style="left:22px;top:63px;font-size:2.6px;color:var(--star)">★ 4.2</div><div class="a" style="left:52px;top:63px;font-size:2.4px">Suki</div>
      <div class="a btn" style="left:81px;top:58px;width:25px;height:8px;font-size:2.4px">Add to Cart</div>
    </article>
  </section>

  <section class="screen" style="left:543px;height:386px">
    <div class="a time">9:41</div><div class="a island"></div>
    <svg class="a sys" viewBox="0 0 20 5"><rect x="0" y="3" width="1" height="2" fill="#222"/><rect x="1.6" y="2" width="1" height="3" fill="#222"/><rect x="3.2" y="1" width="1" height="4" fill="#222"/><path d="M7 2.2a3 3 0 0 1 4 0l-2 2.3z" fill="#222"/><rect x="13" y="1" width="6" height="3.4" rx=".8" fill="#222"/></svg>
    <svg class="a back" viewBox="0 0 10 10"><circle cx="5" cy="5" r="4.5" fill="none" stroke="#9aa1aa" stroke-width=".5"/><path d="M6.5 5H3.5M5 3.5 3.5 5 5 6.5" fill="none" stroke="#9aa1aa" stroke-width=".5"/></svg>
    <div class="a page-title">Order Details</div>

    <div class="a" style="left:6px;top:42px;width:110px;height:31px;border-radius:3px;box-shadow:0 1px 2px rgba(0,0,0,.08)"></div>
    <div class="a bowl" role="img" aria-label="Dream on Salad bowl photo" style="left:12px;top:43px;width:30px;height:28px"></div>
    <div class="a order-name" style="top:50px">Dream on Salad</div>
    <div class="a order-price" style="top:59px">$15 <span>/ item</span></div>
    <div class="a qty" style="left:82px;top:61px"><b>+</b><span>2</span><b>–</b></div>
    <div class="a" style="right:8px;top:44px;width:5px;height:5px;border-radius:50%;background:#cfd2d6"></div>

    <div class="a" style="left:6px;top:81px;width:110px;height:31px;border-radius:3px;box-shadow:0 1px 2px rgba(0,0,0,.08)"></div>
    <div class="a bowl" role="img" aria-label="Kale Ceasar Salad bowl photo" style="left:12px;top:82px;width:30px;height:28px"></div>
    <div class="a order-name" style="top:89px">Kale Ceasar Salad</div>
    <div class="a order-price" style="top:98px">$12 <span>/ item</span></div>
    <div class="a qty" style="left:82px;top:100px"><b>+</b><span>2</span><b>–</b></div>
    <div class="a" style="right:8px;top:83px;width:5px;height:5px;border-radius:50%;background:#cfd2d6"></div>

    <div class="a" style="left:6px;top:120px;width:110px;height:31px;border-radius:3px;box-shadow:0 1px 2px rgba(0,0,0,.08)"></div>
    <div class="a bowl" role="img" aria-label="True Salad bowl photo" style="left:12px;top:121px;width:30px;height:28px"></div>
    <div class="a order-name" style="top:128px">True Salad</div>
    <div class="a order-price" style="top:137px">$12 <span>/ item</span></div>
    <div class="a qty" style="left:82px;top:139px"><b>+</b><span>1</span><b>–</b></div>
    <div class="a" style="right:8px;top:122px;width:5px;height:5px;border-radius:50%;background:#cfd2d6"></div>

    <div class="a field" style="left:6px;top:157px;width:110px">Address</div>
    <div class="a sum" style="top:179px"><span>Total Price</span><span>$66</span></div>
    <div class="a sum" style="top:188px"><span>Discount</span><span>$0</span></div>
    <div class="a sum" style="top:197px;font-weight:500;color:var(--ink)"><span>Payment Amount</span><span>$66</span></div>

    <div class="a" style="left:0;top:217px;width:122px;height:169px;background:var(--panel)"></div>
    <div class="a tiny" style="left:0;width:122px;text-align:center;top:226px;font-size:3px">Add Debit or Credit Card</div>
    <div class="a" style="left:6px;top:238px;width:110px;height:69px;border-radius:2px;background:linear-gradient(135deg,#c1407a 0%,#8a4fb0 50%,#3f6fd6 100%);color:#fff">
      <div class="a" style="left:8px;top:5px;font-size:3.2px;font-weight:600">Debit.</div>
      <div class="a" style="right:9px;top:5px;font-size:4px;font-weight:600;text-align:right;line-height:3.4px">Bank Name<br><span style="font-size:2.4px">&amp; Logo</span></div>
      <div class="a" style="left:8px;top:22px;width:9px;height:7px;border-radius:1px;background:#e8c25a"></div>
      <div class="a" style="left:8px;top:33px;font-size:7px;letter-spacing:.3px;word-spacing:4px;white-space:nowrap">5355 0348 5945 5045</div>
      <div class="a" style="left:8px;top:48px;font-size:3.2px"><span style="font-size:1.6px">VALID THRU</span>&nbsp; 12/24</div>
      <div class="a card-holder">TOBI ANSELM</div>
      <div class="a" style="right:8px;top:52px;width:9px;height:9px;border-radius:50%;background:#f39c2b"></div>
    </div>
    <div class="a field" style="left:6px;top:313px;width:110px">Card Number</div>
    <div class="a field" style="left:6px;top:328px;width:53px">Valid Thru</div>
    <div class="a field" style="left:62px;top:328px;width:54px">CVV</div>
    <div class="a btn" style="left:6px;top:350px;width:110px;height:13px;font-size:5px;font-weight:500">Checkout</div>
  </section>

  <section class="screen" style="left:676px;height:265px;background:linear-gradient(180deg,#fff 0%,#fff 45%,#eef0e6 100%)">
    <div class="a time">9:41</div><div class="a island"></div>
    <svg class="a sys" viewBox="0 0 20 5"><rect x="0" y="3" width="1" height="2" fill="#222"/><rect x="1.6" y="2" width="1" height="3" fill="#222"/><rect x="3.2" y="1" width="1" height="4" fill="#222"/><path d="M7 2.2a3 3 0 0 1 4 0l-2 2.3z" fill="#222"/><rect x="13" y="1" width="6" height="3.4" rx=".8" fill="#222"/></svg>
    <svg class="a" style="left:99px;top:31px;width:9px;height:9px" viewBox="0 0 10 10"><circle cx="5" cy="5" r="5" fill="var(--ink)"/><path d="M3.3 3.3 6.7 6.7M6.7 3.3 3.3 6.7" stroke="#fff" stroke-width=".8"/></svg>
    <div class="a" style="left:0;width:122px;top:56px;text-align:center;font-size:10px;font-weight:600;line-height:12.5px">Thank you<br>for choosing us!</div>
    <div class="a" style="left:8px;width:106px;top:97px;text-align:center;font-size:5.2px;font-weight:300;line-height:6.8px;color:var(--ink-soft)">We’re delighted to have you onboard, and we hope our diverse range of salad recipes brings a burst of flavor and nutrition to your meals. Enjoy creating delicious and healthy salads with ease!</div>
    <div class="a" style="left:0;width:122px;top:172px;text-align:center;font-size:7px;font-weight:600;color:var(--ink)">Greenbowl</div>
    <div class="a home-bar"></div>
  </section>

  <div class="a ghost-mark" style="top:860px;font-size:96px;letter-spacing:-1px">Greenbowl</div>

</main>
</body>
</html>
```